Business card for Brimvault company

Hello Designers,

We need a business card design for a new company based in Moscow.
The name of company - Brimvault (Cargo + Architecture).

We are small construction company that providing following services:

- Development of creative projects based on shipping containers

- Building houses/restorants/bars/shops e.t.c of shipping containers

We are first company in Moscow, that is developing projects and constructing buildings made of shipping containers.
We want people to know that common shipping container is so much more than just a container. With our creative view of things, we will transform a simple box into a successful business.

You can find our logo and examples of what we like in attachment.

Information that must be on card:
1. Name and surname
2. mobile phone number
3. email
4. Website (www.brimvault-build.example)

Please notice that we are Russian company, and we need names in Russian. In attachment in file "Information" you can find the correct spelling.

Requirements
Must have
• Information that must be on card:
• 1. Name and surname
• 2. mobile phone number
• 3. email
• 4. Website (www.brimvault-build.example)
Nice to have
• Elegant design, clean, modern and interesting.

```html
<!DOCTYPE html>
<html lang="ru">
<head>
<meta charset="utf-8">
<title>Brimvault — business card</title>
<link rel="stylesheet" href="https://fonts.googleapis.com/css2?family=Open+Sans:wght@400;600;700&display=swap">
<style>
  :root {
    --backdrop: #e9e7e4;
    --card-dark: #232325;
    --card-light: #ffffff;
    --ink: #1d1d1f;
    --emboss: #48484b;
    --accent-square: #d4d5d8;
    --accent-square-dark: #4e4f52;
  }
  * { margin: 0; padding: 0; box-sizing: border-box; }
  html, body { width: 1200px; height: 1000px; overflow: hidden; }
  body {
    position: relative;
    background: var(--backdrop);
    font-family: "Open Sans", Arial, sans-serif;
    color: var(--ink);
  }
  .card {
    position: absolute;
    left: 265px;
    width: 665px;
    height: 397px;
  }
  .card--front {
    top: 73px;
    background: var(--card-dark);
  }
  .card--back {
    top: 533px;
    background: var(--card-light);
  }
  .wordmark {
    position: absolute;
    left: 0; right: 0;
    display: flex;
    align-items: center;
    justify-content: center;
    gap: 18px;
    font-weight: 400;
    letter-spacing: 2px;
  }
  .wordmark__square { display: block; }
  .card--front .wordmark {
    top: 190px;
    font-size: 54px;
    color: var(--emboss);
  }
  .card--front .wordmark__square { width: 34px; height: 34px; background: var(--accent-square-dark); }
  .card--back .wordmark {
    top: 105px;
    font-size: 38px;
    color: var(--ink);
  }
  .card--back .wordmark__square { width: 26px; height: 26px; background: var(--accent-square); }
  .website {
    position: absolute;
    top: 222px;
    left: 0; right: 0;
    text-align: center;
    font-size: 15px;
  }
  .website strong { font-weight: 600; }
  .contacts {
    position: absolute;
    top: 281px;
    left: 0; right: 0;
    display: grid;
    grid-template-columns: 1fr 1fr;
  }
  .contacts::after {
    content: "";
    position: absolute;
    left: 332px;
    top: 4px;
    width: 1px;
    height: 78px;
    background: var(--ink);
  }
  .person { font-size: 14.5px; line-height: 22px; }
  .person--left { text-align: right; padding-right: 352px; padding-right: 352px; }
  .person--left { padding-right: 352px; }
  .person--right { padding-left: 352px; }
  .person { position: absolute; width: 332px; }
  .person--left { left: 0; padding-right: 19px; }
  .person--right { left: 333px; padding-left: 19px; text-align: left; }
  .person__name { font-size: 17px; font-weight: 600; margin-bottom: 13px; }
  .person__line { display: flex; align-items: center; gap: 7px; }
  .person--left .person__line { justify-content: flex-end; }
  .icon { width: 12px; height: 12px; flex: none; fill: var(--ink); }
</style>
</head>
<body>

<section class="card card--front" aria-label="Front side">
  <div class="wordmark"><span class="wordmark__square"></span><span>Brimvault</span></div>
</section>

<section class="card card--back" aria-label="Back side">
  <div class="wordmark"><span class="wordmark__square"></span><span>Brimvault</span></div>

  <p class="website">www.<strong>brimvault-build</strong>.example</p>

  <div class="contacts">
    <div class="person person--left">
      <p class="person__name">Арутюнян Давид</p>
      <p class="person__line">+79001234567
        <svg class="icon" viewBox="0 0 12 12" aria-hidden="true"><path d="M2 1.5c3.5 0 7.5 3.6 8.5 8.8l-2 .9-1.2-2.4 1-.7C7.6 6.1 5.8 4.4 3.8 3.8l-.6 1L1 3.6z"/></svg>
      </p>
      <p class="person__line">arutyunyan@brimvault.example
        <svg class="icon" viewBox="0 0 12 12" aria-hidden="true"><path d="M1 2.5h10v7H1z M1.6 3l4.4 3.6L10.4 3" fill="none" stroke="#1d1d1f" stroke-width="1.2"/><rect x="1" y="2.5" width="10" height="7"/><path d="M1.5 3l4.5 3.5L10.5 3" fill="none" stroke="#fff" stroke-width="1"/></svg>
      </p>
    </div>
    <div class="person person--right">
      <p class="person__name">Мельников Олег</p>
      <p class="person__line">
        <svg class="icon" viewBox="0 0 12 12" aria-hidden="true"><path d="M10 1.5C6.5 1.5 2.5 5.1 1.5 10.3l2 .9 1.2-2.4-1-.7C4.4 6.1 6.2 4.4 8.2 3.8l.6 1L11 3.6z"/></svg>
        +79007654321</p>
      <p class="person__line">
        <svg class="icon" viewBox="0 0 12 12" aria-hidden="true"><rect x="1" y="2.5" width="10" height="7"/><path d="M1.5 3l4.5 3.5L10.5 3" fill="none" stroke="#fff" stroke-width="1"/></svg>
        melnikov@brimvault.example</p>
    </div>
  </div>
</section>

</body>
</html>
```